Flyer-Design für regional agierendes Immobilienbüro
Zielgruppe
*regional agierendes Immobilienbüro
*Vermittlung von privaten Wohnimmobilien (Einfamilienhäuser, Wohnungen, Grundstücke)
*projektbezogene Zielgruppe: Immobilien Eigentümer / Verkäufer /Vermieter
*Idee: Gutschein über eine von drei Serviceleistungen - kostenlos*:
- Wertermittlung vom geprüften Preisbild-Berater
- Wohnflächen-Check
- Unterlagen-Check
*für Verkäufer / Vermieter im Wert von EUR 349,-
Aufgabenstellung
*CI (Style Guide, diverse Grafiken und Logos in verschiedenen Formaten vorhanden)
*cleanes, modernes Design - dennoch Eyecatcher (Postwurf)
*Ggf. DIN lang
Der Schlüssel zu einem erfolgreichen Verkauf liegt in der sorgfältigen Vorbereitung!
Passt der Verkaufspreis?
Sind alle Unterlagen vollständig und vorab auf mögliche 'Stolpersteine' geprüft?
Stimmt die Wohnfläche und sind alle Angaben rechtssicher korrekt?
Gerne prüfen wir, ob die grundlegenden Voraussetzungen für einen reibungslosen Verkauf Ihrer Immobilie zum bestmöglichen Verkaufspreis passen - kostenlos und unverbindlich! Im Rahmen eines unverbindlichen Beratungsgesprächs erfahren Sie auch, wie Sie von unserem vollumfänglichen Vermarktungsservice profitieren können.
Rufen Sie am besten gleich an und vereinbaren Sie einen Termin mit uns!

```html
<!DOCTYPE html>
<html lang="de">
<head>
<meta charset="utf-8">
<title>WALDHOFER Immobilien – Flyer DIN lang</title>
<link href="https://fonts.googleapis.com/css2?family=Fira+Sans+Extra+Condensed:ital,wght@0,400;0,500;1,400;1,600;1,700&display=swap" rel="stylesheet">
<style>
  :root {
    --teal-dark: #03506b;
    --teal-light: #3b7b97;
    --gold-light: #d8a96c;
    --gold-dark: #9a7a50;
    --white: #ffffff;
    --photo-portrait: #9a9a9c;
    --photo-desk: #5d6d70;
  }
  * { margin: 0; padding: 0; box-sizing: border-box; }
  html, body { width: 1200px; height: 1200px; overflow: hidden; background: var(--white); }
  body { position: relative; font-family: "Fira Sans Extra Condensed", "Arial Narrow", sans-serif; color: var(--white); }

  .flyer {
    position: absolute; top: 235px; width: 350px; height: 736px;
    box-shadow: 3px 4px 6px rgba(0,0,0,0.25);
    background: var(--white);
  }
  .flyer--front { left: 193px; }
  .flyer--back { left: 663px; }

  .band { position: absolute; left: 0; width: 100%; background: linear-gradient(180deg, var(--teal-dark), var(--teal-light)); }

  /* Front */
  .front-header { top: 0; height: 246px; }
  .brand { position: absolute; top: 60px; left: 0; width: 100%; text-align: center; }
  .brand__square { display: block; width: 70px; height: 70px; margin: 0 auto 22px; border: 1px solid var(--white); }
  .brand__name { font-weight: 400; font-size: 17px; letter-spacing: 14px; padding-left: 14px; }
  .brand__sub { margin-top: 12px; font-weight: 400; font-size: 8px; letter-spacing: 6px; padding-left: 6px; }
  .portrait { position: absolute; top: 248px; left: 0; width: 100%; height: 363px; background: linear-gradient(135deg, #d8d6d2 0%, var(--photo-portrait) 45%, #1f2c45 100%); }
  .front-quote { top: 614px; height: 122px; display: flex; align-items: center; justify-content: center; text-align: center; }
  .front-quote p { font-style: italic; font-size: 17px; line-height: 1.45; }

  /* Back */
  .back-header { top: 0; height: 246px; padding: 17px 17px 0; font-style: italic; font-size: 12.5px; letter-spacing: -0.2px; }
  .back-header p { margin-bottom: 20px; line-height: 1.1; }
  .back-header .question, .back-header .cta { font-weight: 600; }
  .back-header .offer { line-height: 1.4; margin-bottom: 14px; }
  .desk-photo { position: absolute; top: 248px; left: 0; width: 100%; height: 278px; background: linear-gradient(135deg, #4a5a5e 0%, #c8c9c6 45%, var(--photo-desk) 100%); }

  .voucher {
    position: absolute; top: 526px; left: 0; width: 100%; height: 158px;
    background: linear-gradient(90deg, var(--gold-light), var(--gold-dark));
    border-top: 1px dashed var(--white); border-bottom: 1px dashed var(--white);
    padding: 0 17px;
  }
  .voucher__head { display: flex; align-items: center; justify-content: space-between; height: 82px; border-bottom: 2px solid var(--white); margin-bottom: 12px; }
  .voucher__title { font-style: italic; font-weight: 700; font-size: 26px; white-space: nowrap; letter-spacing: -0.3px; }
  .voucher__list { list-style: none; font-style: italic; font-weight: 600; font-size: 13.5px; line-height: 1.4; white-space: nowrap; padding-right: 8px; }
  .voucher__text { font-style: italic; font-weight: 600; font-size: 12.5px; line-height: 1.4; letter-spacing: -0.2px; }
  .voucher__note { font-style: italic; font-size: 9.5px; margin-top: 1px; }
  .scissors { position: absolute; width: 22px; height: 12px; }
  .scissors--top { top: -7px; right: 6px; }
  .scissors--bottom { bottom: -7px; left: 5px; transform: scaleX(-1); }

  .back-footer { top: 684px; height: 52px; text-align: center; font-size: 11px; line-height: 1.4; padding-top: 9px; }
  .back-footer strong { font-weight: 500; }
</style>
</head>
<body>

<section class="flyer flyer--front">
  <header class="band front-header">
    <div class="brand">
      <span class="brand__square"></span>
      <div class="brand__name">WALDHOFER</div>
      <div class="brand__sub">IMMOBILIEN</div>
    </div>
  </header>
  <div class="portrait" role="img" aria-label="Porträtfoto des Maklers im dunklen Anzug vor hellem Hintergrund"></div>
  <div class="band front-quote">
    <p>“Der Schlüssel zu einem erfolgreichen<br>Verkauf Ihrer Immobilie liegt in der<br>sorgfältigen Vorbereitung!”</p>
  </div>
</section>

<section class="flyer flyer--back">
  <div class="band back-header">
    <p>Können Sie diese 3 Fragen mit JA beantworten?</p>
    <p class="question">- Passt der von Ihnen ermittelte Verkaufspreis?</p>
    <p class="question">- Stimmt die Wohnfläche und sind alle Angaben rechtssicher?</p>
    <p class="question">- Sind alle Unterlagen vollständig und auf Stolpersteine geprüft?</p>
    <p class="offer">Wir bieten mit unserem Gutschein Hilfestellung bei der Beantwortung<br>dieser Fragen. Für Sie vollkommen unverbindlich und kostenlos!</p>
    <p class="cta">Jetzt Gutschein einlösen und Sicherheit schaffen!</p>
  </div>
  <div class="desk-photo" role="img" aria-label="Foto: Hände mit Füller über einem Lageplan auf dem Schreibtisch"></div>

  <div class="voucher">
    <svg class="scissors scissors--top" viewBox="0 0 22 12" aria-hidden="true"><g fill="none" stroke="#fff" stroke-width="1.5"><circle cx="18" cy="3" r="2.5"/><circle cx="18" cy="9" r="2.5"/><path d="M16 4 L1 9 M16 8 L1 3"/></g></svg>
    <div class="voucher__head">
      <div class="voucher__title">GUTSCHEIN ÜBER:</div>
      <ul class="voucher__list">
        <li>- WERTERMITTLUNG</li>
        <li>- WOHNFLÄCHEN-CHECK</li>
        <li>- UNTERLAGEN-CHECK</li>
      </ul>
    </div>
    <p class="voucher__text">Mit diesem Gutschein erhalten Verkäufer / Vermieter eine der 3<br>oben genannten Serviceleistungen im Wert von 349 € kostenlos!</p>
    <p class="voucher__note">Gültig bis 31.12.2018, keine Barauszahlung möglich.</p>
    <svg class="scissors scissors--bottom" viewBox="0 0 22 12" aria-hidden="true"><g fill="none" stroke="#fff" stroke-width="1.5"><circle cx="18" cy="3" r="2.5"/><circle cx="18" cy="9" r="2.5"/><path d="M16 4 L1 9 M16 8 L1 3"/></g></svg>
  </div>

  <footer class="band back-footer">
    <div>WALDHOFER Immobilien | Jonas Lindner | Lindenweg 7 | 54321 Beispielstadt</div>
    <div><strong>Telefon: 09876 54 32 100</strong> | www.waldhofer-immo.de</div>
  </footer>
</section>

</body>
</html>
```